Design a web site for my business - Brellan Coatworks Mackaby.

We are a family business that handles design, fabrication and installation of powder coated aluminum, stainless steel and glass products. Including handrails, privacy slat screens, electric gates and pool fencing. We are based in the Whitsundays in North Queensland and service an area from Airlie Beach to Townsville.

Target Market(s)

Domestic and commercial

Industry/Entity Type

fabrication - manufacturing

Coding

Coded - Design and coding required

Number of Pages Required

5+ page

Colors
0054AA
0677BA
7BADD7
CADEEF
E8F1F8

Requirements
Must have
• photo galleries, contact page, one page for privacy screens, balustrades, glass fencing, stainless steel handrail, powder coated aluminium handrails and pool fencing

```html
<!DOCTYPE html>
<html lang="en">
<head>
<meta charset="utf-8">
<title>Brellan Coatworks Mackaby</title>
<link href="https://fonts.googleapis.com/css2?family=Lato:wght@400;700;900&family=Roboto:wght@400;500;700&display=swap" rel="stylesheet">
<style>
:root{
  --brand:#0054AA;
  --brand-mid:#0677BA;
  --brand-soft:#7BADD7;
  --brand-pale:#CADEEF;
  --brand-bg:#E8F1F8;
  --dark:#15263a;
  --ink:#1f2a36;
  --text:#3f4853;
  --white:#fff;
}
*{margin:0;padding:0;box-sizing:border-box}
html,body{width:1200px;height:4383px;overflow:hidden}
body{font-family:'Roboto',sans-serif;color:var(--text);background:var(--white);position:relative}
.abs{position:absolute}
.heading{font-family:'Lato',sans-serif;font-weight:900;font-size:42px;color:var(--ink);letter-spacing:0.5px;text-align:center}
.heading .light{font-weight:400;color:var(--brand)}
.heading .dark-light{font-weight:400;color:var(--ink)}
.heading-rule{width:76px;height:3px;background:var(--brand);margin:6px auto 0}
.btn{position:absolute;background:var(--brand);color:#fff;font-family:'Roboto',sans-serif;font-weight:500;font-size:15px;display:flex;align-items:center;justify-content:center;letter-spacing:.3px}

/* top bar */
.topbar{left:0;top:0;width:1200px;height:41px;background:var(--dark)}
.topbar .social{top:0;width:34px;height:41px;display:flex;align-items:center;justify-content:center}
.topbar .social span{width:10px;height:10px;border-radius:50%;background:#fff}
.topbar .email{right:110px;top:0;height:41px;display:flex;align-items:center;gap:10px;color:#fff;font-size:15px}

/* header */
.header{left:0;top:41px;width:1200px;height:94px;background:#fff}
.logo{font-family:'Lato',sans-serif;font-weight:900;color:var(--brand);white-space:nowrap}
.nav{left:434px;top:0;height:94px;display:flex;align-items:center;gap:27px;font-size:14.5px;font-weight:500;color:var(--ink)}
.nav .active{color:var(--brand);border-bottom:2px solid var(--brand);padding-bottom:3px}
.call{left:898px;top:0;width:302px;height:94px;background:var(--brand);clip-path:polygon(64px 0,100% 0,100% 100%,0 100%)}
.call .label{left:124px;top:24px;color:#fff;font-size:13px}
.call .num{left:124px;top:44px;color:#fff;font-size:18px;font-weight:700}

/* hero */
.hero{left:0;top:135px;width:1200px;height:665px;background:linear-gradient(180deg,#8a8a82 0%,#a3a092 22%,#6f7660 45%,#4d6a52 58%,#4a7590 72%,#8a8f92 100%)}
.hero-title{left:0;top:272px;width:1200px;text-align:center;font-family:'Lato',sans-serif;font-weight:700;font-size:38px;line-height:48px;color:#fff}
.hero-sub{left:270px;top:380px;width:660px;text-align:center;font-size:20px;line-height:27px;color:#fff}
.dots{left:1141px;top:371px;display:flex;flex-direction:column;gap:9px}
.dots span{width:12px;height:12px;border:2px solid #fff;border-radius:50%}
.dots .on{background:#fff}

/* about */
.about-title{left:660px;top:876px;font-family:'Lato',sans-serif;font-weight:900;font-size:42px;color:var(--ink)}
.about-title .light{font-weight:400;color:var(--brand)}
.about-rule{left:662px;top:929px;width:150px;height:2px;background:var(--brand)}
.about-text{left:661px;top:955px;width:431px;font-size:16px;line-height:25.5px;color:var(--text);text-align:justify}
.about-text p+p{margin-top:15px}

/* services */
.services{left:0;top:1456px;width:1200px;height:640px;background:var(--brand-bg)}
.svc{top:1632px;width:265px;height:359px;overflow:hidden}
.svc-label{left:0;bottom:30px;width:100%;text-align:center;color:#fff;font-weight:700;font-size:16px}
.svc-overlay{inset:0;background:rgba(20,35,55,.75)}
.svc-body{left:0;top:62px;width:100%;text-align:center;color:#fff}
.svc-body h3{font-size:17px;font-weight:700}
.svc-body p{font-size:14px;line-height:26px;margin:12px 18px 0}
.svc-body a{display:inline-block;margin-top:12px;color:var(--brand-soft);font-size:14px;text-decoration:underline}
.arrow{top:1800px}

/* testimonials */
.testi-card{top:2322px;width:299px;height:330px;background:#fff;border-radius:12px}
.testi-card .q{left:15px;top:16px;font-family:'Lato',sans-serif;font-weight:900;font-size:52px;line-height:52px;color:var(--ink)}
.testi-card .stars{left:36px;top:57px;color:var(--brand);font-size:20px;letter-spacing:2px}
.testi-card .body{left:36px;top:100px;width:242px;font-size:14px;line-height:22px;color:var(--text)}
.testi-card .line{left:36px;top:270px;width:38px;height:2px;background:var(--brand)}
.testi-card .name{left:36px;top:283px;font-size:14px;font-weight:700;color:var(--ink)}
.pager{left:568px;top:2696px;display:flex;gap:9px}
.pager span{width:6px;height:6px;border-radius:50%;background:rgba(255,255,255,.5)}
.pager .on{background:#fff}

/* projects */
.proj{top:2934px;width:352px;height:325px}
.proj-caption{top:3290px;width:352px;text-align:center;font-size:19px;font-weight:700;line-height:29px;color:var(--ink)}
.proj-caption.active{color:var(--brand);text-decoration:underline}

/* contact */
.contact{left:0;top:3416px;width:1200px;height:967px;background:var(--brand-bg)}
.field{width:409px;height:49px;background:#fff;border-radius:25px;display:flex;align-items:center;box-shadow:0 1px 6px rgba(0,0,0,.05)}
.field .ico{width:52px;height:100%;display:flex;align-items:center;justify-content:center;border-right:1px solid #ddd}
.field .ph{padding-left:16px;font-size:15px;color:#444}
.message{left:606px;top:3578px;width:412px;height:180px;background:#fff;border-radius:22px;box-shadow:0 1px 6px rgba(0,0,0,.05)}

/* footer */
.foot-h{font-size:15px;font-weight:700;color:#fff;letter-spacing:.3px}
.foot-rule{height:2px;background:var(--brand-soft);margin-top:9px}
.foot-txt{font-size:13.5px;line-height:22px;color:#fff}
.foot-links{font-size:13.5px;color:#fff;line-height:36px}
.foot-ico{width:36px;height:36px;border-radius:50%;background:#fff;display:flex;align-items:center;justify-content:center}
.news{left:829px;top:4122px;width:260px;height:46px;background:#fff;border-radius:2px;display:flex;align-items:center;justify-content:space-between;padding:0 16px;font-size:14px;color:#444}
.soc{width:34px;height:34px;border-radius:50%;background:#fff}
.copy{left:0;top:4333px;width:1200px;text-align:center;font-size:13px;color:#fff}
</style>
</head>
<body>

<!-- top bar -->
<div class="abs topbar">
  <div class="abs social" style="left:111px;background:var(--brand)"><span></span></div>
  <div class="abs social" style="left:145px"><span></span></div>
  <div class="abs social" style="left:179px"><span></span></div>
  <div class="abs email">
    <svg width="16" height="12" viewBox="0 0 16 12"><rect width="16" height="12" rx="1" fill="#7BADD7"/><path d="M0 1l8 6 8-6" stroke="#15263a" stroke-width="1.6" fill="none"/></svg>
    Send us an Email
  </div>
</div>

<!-- header -->
<header class="abs header">
  <div class="abs logo" style="left:109px;top:34px;font-size:21px">Brellan Coatworks Mackaby</div>
  <nav class="abs nav">
    <span class="active">HOME</span><span>ABOUT US</span><span>SERVICES</span><span>PROJECTS</span><span>CONTACT US</span>
  </nav>
  <div class="abs call">
    <svg class="abs" style="left:72px;top:28px" width="40" height="40" viewBox="0 0 24 24"><path fill="#fff" d="M6.6 10.8c1.4 2.8 3.8 5.1 6.6 6.6l2.2-2.2c.3-.3.7-.4 1-.2 1.1.4 2.3.6 3.6.6.6 0 1 .4 1 1V20c0 .6-.4 1-1 1C10.6 21 3 13.4 3 4c0-.6.4-1 1-1h3.5c.6 0 1 .4 1 1 0 1.3.2 2.5.6 3.6.1.3 0 .7-.2 1z"/><path d="M14 3a7 7 0 017 7M14 6.5a3.5 3.5 0 013.5 3.5" stroke="#fff" stroke-width="1.6" fill="none"/></svg>
    <div class="abs label">Call Us Today</div>
    <div class="abs num">+61 000 000 0000</div>
  </div>
</header>

<!-- hero -->
<section class="abs hero" role="img" aria-label="Modern home with glass pool fencing around a swimming pool at sunset"></section>
<div class="abs hero-title">PREMIUM ALUMINIUM, STAINLESS<br>STEEL &amp; GLASS SOLUTIONS</div>
<div class="abs hero-sub">Custom-designed, expertly fabricated, and professionally installed solutions for homes and businesses across the Whitsundays and North Queensland.</div>
<div class="btn" style="left:504px;top:485px;width:190px;height:46px">GET A FREE QUOTE</div>
<div class="abs dots"><span></span><span class="on"></span><span></span><span></span></div>
<svg class="abs" style="left:0;top:600px" width="1200" height="200" viewBox="0 600 1200 200">
  <polygon points="0,800 0,795 600,650 1200,795 1200,800" fill="#fff"/>
  <polygon points="153,762 600,621 1042,762 600,660" fill="var(--brand)"/>
</svg>

<!-- about -->
<svg class="abs" style="left:106px;top:1013px" width="368" height="330" viewBox="0 0 368 330">
  <polyline points="73,5 5,5 5,325 362,325 362,255" fill="none" stroke="var(--brand)" stroke-width="10"/>
</svg>
<div class="abs" style="left:191px;top:843px;width:291px;height:328px;background:linear-gradient(160deg,#9a8a4a,#5c6b3c 45%,#6b6a5a 70%,#a39468)" role="img" aria-label="Garden with horizontal slat privacy fence and ornamental grasses"></div>
<div class="abs" style="left:344px;top:1006px;width:233px;height:257px;background:#fff"></div>
<div class="abs" style="left:352px;top:1013px;width:218px;height:243px;background:linear-gradient(180deg,#5d6e96,#3f4a5a 40%,#2c2a25 70%,#8a6a3a)" role="img" aria-label="Black aluminium gate with garden lighting at dusk"></div>
<div class="abs about-title">ABOUT <span class="light">US</span></div>
<div class="abs about-rule"></div>
<div class="abs about-text">
  <p>We are a family-owned fabrication and installation company specialising in premium powder-coated aluminium, stainless steel, and glass products. With a commitment to quality workmanship and exceptional customer service, we design, manufacture, and install custom solutions tailored to your property.</p>
  <p>Based in the Whitsundays, we proudly service clients from Airlie Beach to Townsville, delivering durable, stylish, and compliant products for residential and commercial projects.</p>
</div>
<div class="btn" style="left:662px;top:1237px;width:148px;height:45px">LEARN MORE</div>

<!-- services -->
<section class="abs services"></section>
<div class="abs heading" style="left:0;top:1534px;width:1200px"><span class="light">OUR</span> SERVICES<div class="heading-rule"></div></div>
<div class="abs svc" style="left:26px;background:linear-gradient(170deg,#c9d3dc,#8e9aa4 45%,#6d6b5e 80%,#8b7a65)" role="img" aria-label="Balcony with aluminium handrails overlooking the city"><div class="abs svc-label">ALUMINIUM HANDRAILS</div></div>
<div class="abs svc" style="left:320px;background:linear-gradient(170deg,#555,#3d3a36)" role="img" aria-label="Dark slat privacy screen">
  <div class="abs svc-overlay"></div>
  <div class="abs svc-body">
    <svg width="86" height="86" viewBox="0 0 86 86" style="display:block;margin:-8px auto 0"><rect x="18" y="18" width="50" height="50" transform="rotate(45 43 43)" fill="#fff"/><g fill="var(--brand)"><rect x="30" y="32" width="4" height="22"/><rect x="37" y="32" width="4" height="22"/><rect x="44" y="32" width="4" height="22"/><rect x="51" y="32" width="4" height="22"/><rect x="27" y="37" width="32" height="3"/><rect x="27" y="46" width="32" height="3"/></g></svg>
    <h3 style="margin-top:6px">PRIVACY SLAT SCREENS</h3>
    <p>Enhance privacy while adding a modern architectural feature to your home or business.</p>
    <a>LEARN MORE</a>
  </div>
</div>
<div class="abs svc" style="left:614px;background:linear-gradient(175deg,#9fb7cc,#6c6f6e 35%,#2f2f30 65%,#8f8a82)" role="img" aria-label="Modern house with black electric sliding gate"><div class="abs svc-label">ELECTRIC GATES</div></div>
<div class="abs svc" style="left:909px;background:linear-gradient(170deg,#a7c3d6,#4f7a5a 35%,#2a9aa5 65%,#9b8f80)" role="img" aria-label="Frameless glass pool fence beside a pool deck"><div class="abs svc-label">GLASS POOL FENCING</div></div>
<svg class="abs arrow" style="left:50px" width="42" height="16" viewBox="0 0 42 16"><path d="M41 8H2M9 1L2 8l7 7" stroke="#fff" stroke-width="1.5" fill="none"/></svg>
<svg class="abs arrow" style="left:1108px" width="42" height="16" viewBox="0 0 42 16"><path d="M1 8h39M33 1l7 7-7 7" stroke="#fff" stroke-width="1.5" fill="none"/></svg>

<!-- testimonials -->
<svg class="abs" style="left:0;top:2060px" width="1200" height="712" viewBox="0 2060 1200 712">
  <polygon points="0,2247 600,2095 1200,2247 1200,2772 0,2772" fill="var(--brand)"/>
  <polygon points="153,2211 600,2063 1042,2211 600,2100" fill="var(--brand)"/>
  <polygon points="165,2208 600,2096 1030,2208 600,2117" fill="#fff"/>
</svg>
<div class="abs heading" style="left:0;top:2224px;width:1200px;color:#fff">TESTIMONIALS<div class="heading-rule" style="background:#fff;width:76px"></div></div>

<div class="abs testi-card" style="left:111px">
  <div class="abs q">&ldquo;</div><div class="abs stars">★★★★★</div>
  <div class="abs body">Lorem ipsum dolor sit amet, conse ctetur adipiscing elit, sed do eiusm od tempor incididunt ut labore et dolore magna aliqua. Ut enim ad minim veniam, quis nostrud exercitatio n ullamco laboris nisi ut aliquip ex ea consequat.</div>
  <div class="abs line"></div><div class="abs name">- John Doe</div>
</div>
<div class="abs testi-card" style="left:449px">
  <div class="abs q">&ldquo;</div><div class="abs stars">★★★★★</div>
  <div class="abs body">Lorem ipsum dolor sit amet, conse ctetur adipiscing elit, sed do eiusm od tempor incididunt ut labore et dolore magna aliqua. Ut enim ad minim veniam, quis nostrud exercitatio n ullamco laboris nisi ut aliquip ex ea consequat.</div>
  <div class="abs line"></div><div class="abs name">- John Doe</div>
</div>
<div class="abs testi-card" style="left:788px">
  <div class="abs q">&ldquo;</div><div class="abs stars">★★★★★</div>
  <div class="abs body">Lorem ipsum dolor sit amet, conse ctetur adipiscing elit, sed do eiusm od tempor incididunt ut labore et dolore magna aliqua. Ut enim ad minim veniam, quis nostrud exercitatio n ullamco laboris nisi ut aliquip ex ea consequat.</div>
  <div class="abs line"></div><div class="abs name">- John Doe</div>
</div>
<div class="abs pager"><span></span><span></span><span></span><span class="on"></span><span></span></div>

<!-- projects -->
<div class="abs heading" style="left:0;top:2870px;width:1200px"><span class="light">OUR</span> PROJECTS<div class="heading-rule"></div></div>
<div class="abs proj" style="left:-158px;clip-path:polygon(0 0,100% 24%,100% 100%,0 100%);background:linear-gradient(160deg,#d9d2c6,#a27a55 50%,#6a4a30)" role="img" aria-label="Timber staircase with glass balustrade"></div>
<div class="abs proj" style="left:230px;clip-path:polygon(0 0,100% 24%,100% 100%,0 100%);background:linear-gradient(170deg,#d8cfc4,#a27150 40%,#5a5852 75%,#9a9892)" role="img" aria-label="Timber slat privacy screen beside a paved courtyard"></div>
<div class="abs proj" style="left:618px;clip-path:polygon(0 24%,100% 0,100% 100%,0 100%);background:linear-gradient(170deg,#4f7a3a,#6b8f52 35%,#3c8f94 65%,#b5ada0)" role="img" aria-label="Curved garden pool with glass fencing"></div>
<div class="abs proj" style="left:1006px;clip-path:polygon(0 24%,100% 0,100% 100%,0 100%);background:linear-gradient(170deg,#b9cde0,#e4e6e7 35%,#3a3c3e 60%,#8c8c88)" role="img" aria-label="Black aluminium slat fence in front of a modern house"></div>
<svg class="abs" style="left:50px;top:3119px" width="42" height="16" viewBox="0 0 42 16"><path d="M41 8H2M9 1L2 8l7 7" stroke="#fff" stroke-width="1.5" fill="none"/></svg>
<svg class="abs" style="left:1108px;top:3119px" width="42" height="16" viewBox="0 0 42 16"><path d="M1 8h39M33 1l7 7-7 7" stroke="#fff" stroke-width="1.5" fill="none"/></svg>
<div class="abs proj-caption" style="left:-158px">LOREM IPSUM DOLOR SIT<br>AMET CONSEA</div>
<div class="abs proj-caption" style="left:230px">LOREM IPSUM DOLOR SIT<br>AMET CONSEA</div>
<div class="abs proj-caption active" style="left:618px">LOREM IPSUM DOLOR SIT<br>AMET CONSEA</div>
<div class="abs proj-caption" style="left:1006px">LOREM IPSUM DOLOR SIT<br>AMET CONSEA</div>

<!-- contact -->
<section class="abs contact"></section>
<div class="abs heading" style="left:0;top:3484px;width:1200px">CONTACT <span class="dark-light">US</span><div class="heading-rule"></div></div>
<div class="abs field" style="left:182px;top:3578px"><div class="ico"><svg width="13" height="14" viewBox="0 0 13 14"><circle cx="6.5" cy="4" r="3.5" fill="#333"/><path d="M0 14c0-4 3-6 6.5-6S13 10 13 14z" fill="#333"/></svg></div><span class="ph">Your Name</span></div>
<div class="abs field" style="left:182px;top:3644px"><div class="ico"><svg width="15" height="11" viewBox="0 0 15 11"><rect width="15" height="11" rx="1" fill="#333"/><path d="M0 1l7.5 5L15 1" stroke="#fff" stroke-width="1.3" fill="none"/></svg></div><span class="ph">Email</span></div>
<div class="abs field" style="left:182px;top:3709px"><div class="ico"><svg width="14" height="14" viewBox="0 0 24 24"><path fill="#333" d="M6.6 10.8c1.4 2.8 3.8 5.1 6.6 6.6l2.2-2.2c.3-.3.7-.4 1-.2 1.1.4 2.3.6 3.6.6.6 0 1 .4 1 1V20c0 .6-.4 1-1 1C10.6 21 3 13.4 3 4c0-.6.4-1 1-1h3.5c.6 0 1 .4 1 1 0 1.3.2 2.5.6 3.6.1.3 0 .7-.2 1z"/></svg></div><span class="ph">Phone</span></div>
<div class="abs message">
  <svg class="abs" style="left:22px;top:22px" width="17" height="13" viewBox="0 0 17 13"><ellipse cx="6.5" cy="5" rx="6.5" ry="5" fill="#333"/><ellipse cx="11" cy="8" rx="6" ry="4.5" fill="#333"/></svg>
  <div class="abs" style="left:52px;top:12px;width:1px;height:32px;background:#ddd"></div>
  <div class="abs" style="left:68px;top:19px;font-size:15px;color:#444">Your Message</div>
</div>
<div class="btn" style="left:512px;top:3785px;width:176px;height:48px">SEND MESSAGE</div>

<!-- footer -->
<svg class="abs" style="left:0;top:3890px" width="1200" height="493" viewBox="0 3890 1200 493">
  <polygon points="0,4085 600,3898 1200,4085 1200,4383 0,4383" fill="var(--dark)"/>
  <polygon points="165,4034 600,3918 1030,4034 600,3955" fill="var(--brand-mid)"/>
</svg>
<div class="abs logo" style="left:109px;top:4150px;color:#fff;font-size:28px;line-height:36px;white-space:normal;width:260px">Brellan Coatworks Mackaby</div>

<div class="abs" style="left:400px;top:4055px"><div class="foot-h">CONTACT US</div><div class="foot-rule" style="width:114px"></div></div>
<div class="abs foot-ico" style="left:400px;top:4118px"><svg width="12" height="16" viewBox="0 0 12 16"><path d="M6 0a6 6 0 00-6 6c0 4.5 6 10 6 10s6-5.5 6-10a6 6 0 00-6-6z" fill="var(--brand)"/><circle cx="6" cy="6" r="2.2" fill="#fff"/></svg></div>
<div class="abs foot-txt" style="left:455px;top:4120px">Whitsundays in North<br>Queensland</div>
<div class="abs foot-ico" style="left:400px;top:4178px"><svg width="15" height="15" viewBox="0 0 24 24"><path fill="var(--brand)" d="M6.6 10.8c1.4 2.8 3.8 5.1 6.6 6.6l2.2-2.2c.3-.3.7-.4 1-.2 1.1.4 2.3.6 3.6.6.6 0 1 .4 1 1V20c0 .6-.4 1-1 1C10.6 21 3 13.4 3 4c0-.6.4-1 1-1h3.5c.6 0 1 .4 1 1 0 1.3.2 2.5.6 3.6.1.3 0 .7-.2 1z"/></svg></div>
<div class="abs foot-txt" style="left:455px;top:4180px">Call Us:<br>+61 000 000 0000</div>
<div class="abs foot-ico" style="left:400px;top:4238px"><svg width="14" height="11" viewBox="0 0 15 11"><rect width="15" height="11" rx="1" fill="var(--brand)"/><path d="M0 1l7.5 5L15 1" stroke="#fff" stroke-width="1.3" fill="none"/></svg></div>
<div class="abs foot-txt" style="left:455px;top:4240px">Email Us:<br><span style="text-decoration:underline">Send us an email</span></div>

<div class="abs" style="left:655px;top:4055px"><div class="foot-h">QUICK LINKS</div><div class="foot-rule" style="width:114px"></div></div>
<div class="abs foot-links" style="left:656px;top:4112px">Home<br>About Us<br>Services<br>Projects<br>Contact Us</div>

<div class="abs" style="left:829px;top:4055px"><div class="foot-h">NEWSLETTER</div><div class="foot-rule" style="width:114px"></div></div>
<div class="abs news">Email Address<svg width="15" height="14" viewBox="0 0 15 14"><path d="M0 6L15 0 11 14 7 9z" fill="var(--brand)"/></svg></div>
<div class="abs soc" style="left:829px;top:4198px;background:var(--brand-mid)"></div>
<div class="abs soc" style="left:870px;top:4198px"></div>
<div class="abs soc" style="left:909px;top:4198px"></div>

<div class="abs" style="left:0;top:4315px;width:1200px;height:1px;background:rgba(255,255,255,.15)"></div>
<div class="abs copy">Copyright © 2026 &nbsp;/&nbsp; All Rights Reserved &nbsp;/&nbsp; Privacy Policy</div>

</body>
</html>
```